Dental Trade Show Brochure

We need a brochure that is created for dental professionals that will explain how our Compliance Management Platform can help them to simplify, centralize and automate their compliance and other documentation requirements for their practices.

would like the content to be refreshed for dental practices. “EHS” should go away, as healthcare has many compliance requirements, not just health and safety. You are the experts. I am looking for your creative genius to help guide me to the right brochure that has text, imagery and design that will speak to my audience.
Updates

Target Market(s)

Dental Industry

Industry/Entity Type

Dental

Requirements
Must have
• would like the content to be refreshed for dental practices. “EHS” should go away, as healthcare has many compliance requirements, not just health and safety. You are the experts. I am looking for your creative genius to help guide me to the right brochure that has text, imagery and design that will speak to my audience.
Nice to have
• We prefer 1 front/back page over bi or tri fold
Should not have
• Other Industry graphics, design, content.

```html
<!DOCTYPE html>
<html lang="en">
<head>
<meta charset="utf-8">
<title>Clearvale Dental Compliance Brochure</title>
<link href="https://fonts.googleapis.com/css2?family=Montserrat+Alternates:wght@700;800&family=Poppins:wght@400;500;600;700&display=swap" rel="stylesheet">
<style>
:root{
  --stage:#6e6e70;
  --paper:#f3f4f7;
  --navy:#1c1a86;
  --royal:#2d32d4;
  --sky:#8fb0f5;
  --ink:#2a2a3a;
  --muted:#55586a;
  --white:#ffffff;
}
*{box-sizing:border-box;margin:0;padding:0}
html,body{width:1200px;height:2864px;overflow:hidden;background:var(--stage)}
body{font-family:"Poppins",sans-serif;color:var(--ink);display:flex;flex-direction:column;align-items:center;justify-content:space-evenly}
.spread{display:flex;box-shadow:0 14px 40px rgba(0,0,0,.35)}
.page{position:relative;overflow:hidden;background:var(--paper);container-type:inline-size}
.page--large{width:680px;height:962px;box-shadow:0 14px 40px rgba(0,0,0,.35)}
.spread .page{width:540px;height:764px}
.page-art{position:absolute;inset:0;width:100%;height:100%}
.abs{position:absolute}
.brand{display:flex;align-items:center;gap:1.6cqw;font-family:"Poppins",sans-serif;font-weight:500;color:var(--royal);font-size:4.6cqw;line-height:1}
.brand-mark{width:3.6cqw;height:3.6cqw;background:var(--royal);border-radius:.5cqw}
.cover-title{font-family:"Montserrat Alternates",sans-serif;font-weight:800;color:var(--white);font-size:5.6cqw;line-height:1.22;letter-spacing:.02em}
.cover-url{font-family:"Montserrat Alternates",sans-serif;font-weight:700;color:var(--white);font-size:2.7cqw;letter-spacing:.04em}
.back-tagline{font-family:"Montserrat Alternates",sans-serif;font-weight:800;color:var(--navy);font-size:3cqw;line-height:1.2;text-align:center}
.contact-list{list-style:none;color:var(--white);font-family:"Montserrat Alternates",sans-serif;font-weight:700;font-size:2.6cqw;text-align:center}
.contact-list li{display:flex;flex-direction:column;align-items:center;gap:.6cqw;margin-bottom:1.6cqw}
.contact-list svg{width:3cqw;height:3cqw}
.photo{position:absolute}
.hero-band{background:linear-gradient(90deg,#262a96,#3a3fc2);color:var(--white);font-family:"Montserrat Alternates",sans-serif;font-weight:700;font-size:3.6cqw;line-height:1.15;padding:0 6.5cqw;display:flex;align-items:center}
.body-copy{font-size:1.32cqw;line-height:1.5;color:var(--muted)}
.feature-title{font-family:"Montserrat Alternates",sans-serif;font-weight:800;color:var(--navy);font-size:3.9cqw}
.feature-sub{font-weight:500;color:var(--navy);font-size:2.3cqw;line-height:1.25}
.check-list{list-style:none}
.check-list li{display:flex;gap:1.6cqw;align-items:flex-start;font-size:1.45cqw;font-weight:600;color:var(--ink);line-height:1.35;margin-bottom:2.6cqw}
.check-list svg{flex:none;width:2.3cqw;height:2.3cqw;margin-top:.1cqw}
.section-title{font-family:"Montserrat Alternates",sans-serif;font-weight:800;color:var(--navy);font-size:3.6cqw;line-height:1.1}
.topic-title{font-weight:500;color:var(--navy);font-size:2.55cqw;margin-bottom:.8cqw}
.topic-copy{font-size:1.32cqw;line-height:1.48;color:var(--muted);text-align:justify}
.framed{border:.7cqw solid var(--white);box-shadow:0 .4cqw 1.2cqw rgba(0,0,0,.25)}
.side-strip{position:absolute;top:0;right:0;width:25%;height:100%;background:var(--navy)}
.device{border-radius:3cqw;border:1cqw solid #d9dbe3;box-shadow:0 .6cqw 1.6cqw rgba(0,0,0,.25)}
</style>
</head>
<body>

<!-- Front cover, full size -->
<section class="page page--large" aria-label="Front cover">
  <svg class="page-art" viewBox="0 0 600 848" preserveAspectRatio="none" aria-hidden="true">
    <rect width="600" height="848" fill="#f3f4f7"/>
    <polygon points="0,290 600,440 600,848 0,848" fill="#2d32d4"/>
    <polygon points="0,310 600,462 600,848 0,848" fill="#1c1a86"/>
    <path d="M0,780 C140,740 300,800 600,760 L600,848 L0,848 Z" fill="#2529b0"/>
    <polygon points="215,270 302,118 498,118 585,270 498,422 302,422" fill="#ffffff" stroke="#8fb0f5" stroke-width="14" stroke-linejoin="round"/>
  </svg>
  <svg class="abs" style="left:0;top:0;width:100%;height:100%" viewBox="0 0 600 848" preserveAspectRatio="none" role="img" aria-label="Photo: dentist treating a patient in the dental chair">
    <defs><linearGradient id="heroA" x1="0" y1="0" x2="1" y2="1"><stop offset="0" stop-color="#5d7fb8"/><stop offset=".55" stop-color="#c9a48f"/><stop offset="1" stop-color="#e4e6ea"/></linearGradient></defs>
    <polygon points="240,270 315,140 485,140 560,270 485,400 315,400" fill="url(#heroA)"/>
  </svg>
  <div class="brand abs" style="left:60%;top:6.5%"><span class="brand-mark"></span>Clearvale</div>
  <h1 class="cover-title abs" style="left:6%;top:58%">Optimize Your Business<br>Operations with the<br>Right Tools</h1>
  <p class="cover-url abs" style="left:6%;top:80%">www.clearvale.cloud</p>
</section>

<!-- Outer spread: back and front covers -->
<div class="spread">
  <section class="page" aria-label="Back cover">
    <svg class="page-art" viewBox="0 0 600 848" preserveAspectRatio="none" aria-hidden="true">
      <rect width="600" height="848" fill="#f3f4f7"/>
      <polygon points="0,200 600,410 600,848 0,848" fill="#2d32d4"/>
      <polygon points="0,222 600,436 600,848 0,848" fill="#1c1a86"/>
      <path d="M0,780 C140,740 300,800 600,760 L600,848 L0,848 Z" fill="#2529b0"/>
      <polygon points="70,285 165,120 375,120 470,285 375,450 165,450" fill="#ffffff" stroke="#8fb0f5" stroke-width="14" stroke-linejoin="round"/>
    </svg>
    <div class="brand abs" style="left:38%;top:6.5%"><span class="brand-mark"></span>Clearvale</div>
    <p class="back-tagline abs" style="left:24%;top:19.5%;width:42%">We Create Software Solutions That Make Dental Practices More Compliant</p>
    <div class="abs" role="img" aria-label="Illustration: desktop monitor showing the compliance dashboard" style="left:23%;top:36%;width:33%;height:14%;border-radius:1cqw;background:linear-gradient(160deg,#dfe5f3,#9aa8c6)"></div>
    <ul class="contact-list abs" style="left:20%;top:59%;width:48%">
      <li><svg viewBox="0 0 24 24" fill="#fff"><path d="M6.6 10.8a15 15 0 0 0 6.6 6.6l2.2-2.2a1 1 0 0 1 1-.25 11.4 11.4 0 0 0 3.6.57 1 1 0 0 1 1 1V20a1 1 0 0 1-1 1A17 17 0 0 1 3 4a1 1 0 0 1 1-1h3.5a1 1 0 0 1 1 1c0 1.25.2 2.45.57 3.57a1 1 0 0 1-.25 1z"/></svg>+1 800-555-0142</li>
      <li><svg viewBox="0 0 24 24"><path d="M3 5h18v14H3z" fill="none" stroke="#fff" stroke-width="2"/><path d="M3 6l9 7 9-7" fill="none" stroke="#fff" stroke-width="2"/></svg>hello@clearvale.cloud</li>
      <li><svg viewBox="0 0 24 24" fill="#fff"><path d="M12 2a7 7 0 0 0-7 7c0 5 7 13 7 13s7-8 7-13a7 7 0 0 0-7-7zm0 9.5A2.5 2.5 0 1 1 12 6.5a2.5 2.5 0 0 1 0 5z"/></svg>Riverton, CA Lakeport, FL</li>
    </ul>
    <p class="cover-url abs" style="left:8%;top:89%">www.clearvale.cloud</p>
  </section>

  <section class="page" aria-label="Front cover">
    <svg class="page-art" viewBox="0 0 600 848" preserveAspectRatio="none" aria-hidden="true">
      <rect width="600" height="848" fill="#f3f4f7"/>
      <polygon points="0,290 600,440 600,848 0,848" fill="#2d32d4"/>
      <polygon points="0,310 600,462 600,848 0,848" fill="#1c1a86"/>
      <path d="M0,780 C140,740 300,800 600,760 L600,848 L0,848 Z" fill="#2529b0"/>
      <polygon points="215,270 302,118 498,118 585,270 498,422 302,422" fill="#ffffff" stroke="#8fb0f5" stroke-width="14" stroke-linejoin="round"/>
    </svg>
    <svg class="abs" style="left:0;top:0;width:100%;height:100%" viewBox="0 0 600 848" preserveAspectRatio="none" role="img" aria-label="Photo: dentist treating a patient in the dental chair">
      <defs><linearGradient id="heroB" x1="0" y1="0" x2="1" y2="1"><stop offset="0" stop-color="#5d7fb8"/><stop offset=".55" stop-color="#c9a48f"/><stop offset="1" stop-color="#e4e6ea"/></linearGradient></defs>
      <polygon points="240,270 315,140 485,140 560,270 485,400 315,400" fill="url(#heroB)"/>
    </svg>
    <div class="brand abs" style="left:60%;top:6.5%"><span class="brand-mark"></span>Clearvale</div>
    <h2 class="cover-title abs" style="left:6%;top:58%">Optimize Your Business<br>Operations with the<br>Right Tools</h2>
    <p class="cover-url abs" style="left:6%;top:80%">www.clearvale.cloud</p>
  </section>
</div>

<!-- Inner spread -->
<div class="spread">
  <section class="page" aria-label="Inside left page">
    <div class="photo" role="img" aria-label="Photo: dental team reviewing records in a modern clinic" style="left:0;top:0;width:100%;height:21%;background:linear-gradient(180deg,#4a5a72,#27324a)"></div>
    <h2 class="hero-band abs" style="left:0;top:21%;width:100%;height:9.5%">A Comprehensive and Affordable Dental<br>Compliance Software Solution</h2>
    <p class="body-copy abs" style="left:6.5%;top:33%;width:85%">Clearvale provides an innovative solution to the many compliance challenges dental practices face, including OSHA and HIPAA requirements, infection control, sterilization logs, radiation safety, staff credentials, audits and inspections, process standardization, and incident response. Our compliance management platform is built on the most secure cloud-based network using the latest cutting edge software technologies. The comprehensive and affordable system can be tailored to your practice, your specialties and your state requirements by our experienced team of dental compliance, Human Resources and Software Developer Professionals.</p>
    <h3 class="feature-title abs" style="left:6.5%;top:49.5%">Features &amp; Benefits</h3>
    <p class="feature-sub abs" style="left:6.5%;top:54%">Reduce Risk and Liability with<br>Efficiency and Visibility</p>
    <ul class="check-list abs" style="left:6.5%;top:60%;width:46%">
      <li><svg viewBox="0 0 24 24"><circle cx="12" cy="12" r="10" fill="none" stroke="#1c1a86" stroke-width="2"/><path d="M7 12.5l3.2 3L17 9" fill="none" stroke="#1c1a86" stroke-width="2"/></svg>Customize audits and inspections.</li>
      <li><svg viewBox="0 0 24 24"><circle cx="12" cy="12" r="10" fill="none" stroke="#1c1a86" stroke-width="2"/><path d="M7 12.5l3.2 3L17 9" fill="none" stroke="#1c1a86" stroke-width="2"/></svg>Monitor and analyze compliance performance across your practice.</li>
      <li><svg viewBox="0 0 24 24"><circle cx="12" cy="12" r="10" fill="none" stroke="#1c1a86" stroke-width="2"/><path d="M7 12.5l3.2 3L17 9" fill="none" stroke="#1c1a86" stroke-width="2"/></svg>Reduce compliance related financial impact and liability.</li>
      <li><svg viewBox="0 0 24 24"><circle cx="12" cy="12" r="10" fill="none" stroke="#1c1a86" stroke-width="2"/><path d="M7 12.5l3.2 3L17 9" fill="none" stroke="#1c1a86" stroke-width="2"/></svg>Increase accountability through assignment of responsibility.</li>
      <li><svg viewBox="0 0 24 24"><circle cx="12" cy="12" r="10" fill="none" stroke="#1c1a86" stroke-width="2"/><path d="M7 12.5l3.2 3L17 9" fill="none" stroke="#1c1a86" stroke-width="2"/></svg>Verify team participation with your audit &amp; inspection programs.</li>
      <li><svg viewBox="0 0 24 24"><circle cx="12" cy="12" r="10" fill="none" stroke="#1c1a86" stroke-width="2"/><path d="M7 12.5l3.2 3L17 9" fill="none" stroke="#1c1a86" stroke-width="2"/></svg>Effectively control the spectrum of practice risks in one location.</li>
    </ul>
    <div class="device abs" role="img" aria-label="Phone showing the Clearvale app home screen" style="left:61%;top:48.5%;width:22%;height:39%;background:linear-gradient(180deg,#eef1fa,#c7d0e6)"></div>
    <div class="brand abs" style="left:6.5%;top:92%"><span class="brand-mark"></span>Clearvale</div>
  </section>

  <section class="page" aria-label="Inside right page">
    <div class="side-strip"></div>
    <h2 class="section-title abs" style="left:8%;top:5.5%;width:55%">Effective Cloud<br>Management Solutions</h2>

    <h3 class="topic-title abs" style="left:8%;top:13.3%">Audits &amp; Inspections</h3>
    <p class="topic-copy abs" style="left:8%;top:16.8%;width:40%">The Audit &amp; Inspection feature allows you to conduct audits, inspections, and infection control checks across every operatory and location using a single, centralized software system. Option for pre-built or custom checklists are available to identify and assign non-conformances and potential hazards, and instantly initiate corrective actions to bring your compliance up to speed. The system allows your practice to ensure regulatory as well as policy and standard compliance.</p>
    <div class="photo framed" role="img" aria-label="Photo: dental office manager reviewing a checklist" style="left:53%;top:13%;width:41%;height:23%;background:linear-gradient(150deg,#6f8fb8,#d5dbe4)"></div>

    <h3 class="topic-title abs" style="left:8%;top:42%">Training Management</h3>
    <p class="topic-copy abs" style="left:8%;top:45.5%;width:40%">The Training Management solution provides the tools to be able to schedule trainings, document and verify training completions, and deliver tailored training content based on individual team roles and requirements. The built-in email notifications remind dentists, hygienists and managers when training deadlines and license renewal dates are upcoming or past due.</p>
    <div class="photo framed" role="img" aria-label="Photo: dental colleagues reviewing training on a tablet" style="left:53%;top:40%;width:41%;height:23%;background:linear-gradient(150deg,#c7ccd6,#f0f1f4)"></div>

    <h3 class="topic-title abs" style="left:8%;top:66.5%">Document Management</h3>
    <p class="topic-copy abs" style="left:8%;top:70%;width:40%">Clearvale is a customized searchable directory and repository for policies, programs, procedures, notifications, audits and other practice documents. A secure Library of all documents, reports, training records, and licenses at your fingertips. Your team has immediate access to materials in one concise location. Documents can be found efficiently with the advanced searchable features. Documents can also be shared quickly with other team members to expedite communication.</p>
    <div class="photo framed" role="img" aria-label="Photo: hand signing a practice document with a pen" style="left:53%;top:66%;width:41%;height:23%;background:linear-gradient(150deg,#d7c4b8,#9c9fa8)"></div>

    <div class="brand abs" style="left:8%;top:92%"><span class="brand-mark"></span>Clearvale</div>
  </section>
</div>

</body>
</html>
```